National Training and assessment company needs a website

Create a 4 page website, simple but professional, the company provides training services to industry, resumes'/ CVs, personnel skill assessment, workplace skills profiling and develops manufactures and supplies training equipment for electrical/engineering training, Company title is Toren K Pty Ltd and also trades under BRW & Associates. letterheads etc all are done using dark green
Reason: Due to work commitments will be interstate from the 26/02 til 05/03/14
Target Market(s)
The market is broad covering the general public, secondary colleges and corporate sector
Industry/Entity Type
Training
Look and feel

```html
<!DOCTYPE html>
<html lang="en">
<head>
<meta charset="utf-8">
<title>Toren K Pty Ltd — Services</title>
<link href="https://fonts.googleapis.com/css2?family=Arimo:wght@400;700&family=Roboto:wght@300&display=swap" rel="stylesheet">
<style>
:root{
  --green:#1e5a3c;
  --green-dark:#174a31;
  --slate:#63666f;
  --slate-dark:#575a63;
  --slate-deep:#51545c;
  --mist:#9fafa6;
  --panel:#eff2f0;
  --ink:#63666f;
  --white:#ffffff;
}
*{margin:0;padding:0;box-sizing:border-box}
html,body{width:1200px;height:949px;overflow:hidden;background:var(--white)}
body{position:relative;font-family:"Arimo",Arial,sans-serif;color:var(--ink)}
.abs{position:absolute}

.brand{left:163px;top:33px;font-size:25px;color:var(--green);letter-spacing:.3px}
.social-top{left:780px;top:38px;display:flex;gap:11px}
.dot{width:14px;height:14px;border-radius:50%;background:#6b6e76}
.divider{left:921px;top:40px;width:1px;height:10px;background:#c4c7cc}
.util-links{right:162px;top:39px;display:flex;gap:12px;font-size:9.5px;color:#55585f}

.nav{left:161px;top:90px;width:878px;height:45px;background:var(--slate);box-shadow:0 10px 12px -8px rgba(0,0,0,.35)}
.nav-home{left:0;top:0;width:45px;height:45px;background:var(--slate-dark);display:flex;align-items:center;justify-content:center}
.nav-links{left:76px;top:16px;font-size:11px;color:var(--white)}
.nav-links span{position:absolute;white-space:nowrap}
.nav-search{right:0;top:0;width:46px;height:45px;background:var(--green);display:flex;align-items:center;justify-content:center}

.title-band{left:161px;top:157px;width:878px;height:68px;background:var(--mist)}
.title-tab{left:0;top:0;width:202px;height:68px;background:var(--green)}
.title-tab h1{position:absolute;left:23px;top:24px;font-size:19px;font-weight:700;color:var(--white)}
.title-notch{left:189px;top:28px;width:0;height:0;border-top:11px solid var(--mist);border-left:13px solid transparent}
.tagline{left:224px;top:22px;font-family:"Roboto",Arial,sans-serif;font-weight:300;font-size:19px;color:var(--white)}
.crumbs{right:22px;top:28px;font-size:11.5px;color:var(--white);word-spacing:10px}

.offer{left:161px;top:247px;width:653px;height:157px;background:var(--panel);padding:20px 23px}
.offer h2{font-size:18px;font-weight:700;margin-bottom:10px}
.offer p{font-size:10.1px;line-height:12.7px;margin-bottom:12px}
.buy{left:836px;top:247px;width:203px;height:157px;background:var(--slate);padding:40px 4px 0 22px;color:var(--white)}
.buy h2{font-size:18px;font-weight:700;margin-bottom:8px}
.buy p{font-size:10.1px;line-height:12.7px}

.service h3{position:absolute;left:0;top:0;font-size:18px;font-weight:700;white-space:nowrap}
.service .icon{position:absolute;left:0;width:68px;height:68px;background:var(--panel);display:flex;align-items:center;justify-content:center}
.service .copy{position:absolute;left:81px;width:352px;font-size:10.1px;line-height:12.7px}
.service .copy p{margin-bottom:12px}

.ticker{left:0;top:748px;width:1200px;height:30px;background:var(--green);color:var(--white)}
.ticker .mark{left:162px;top:8px;width:14px;height:14px;border-radius:50%;background:var(--white)}
.ticker p{position:absolute;left:193px;top:9px;font-size:10.1px}
.ticker b{font-weight:700}
.arrow{top:0;width:30px;height:30px;display:flex;align-items:center;justify-content:center}
.arrow.prev{left:979px;background:var(--green)}
.arrow.next{left:1008px;background:var(--green-dark)}

.footer{left:0;top:778px;width:1200px;height:140px;background:var(--slate);color:var(--white)}
.footer h2{position:absolute;left:161px;top:43px;font-size:18px;font-weight:700}
.footer .lede{position:absolute;left:162px;top:61px;font-size:8px}
.social-foot{left:161px;top:83px;display:flex;gap:16px}
.social-foot .dot{background:var(--white);width:15px;height:15px}
.foot-links{top:65px;font-size:9.5px}
.foot-links span{position:absolute;white-space:nowrap}
.legal{left:0;top:918px;width:1200px;height:31px;background:var(--slate-deep);color:var(--white)}
.legal p{position:absolute;left:161px;top:12px;font-size:7.5px;font-weight:700}
</style>
</head>
<body>

<header>
  <div class="abs brand">Toren K Pty Ltd</div>
  <div class="abs social-top" aria-label="Social links">
    <span class="dot"></span><span class="dot"></span><span class="dot"></span><span class="dot"></span><span class="dot"></span>
  </div>
  <div class="abs divider"></div>
  <nav class="abs util-links"><span>News</span><span>FAQ</span><span>Contact</span></nav>

  <nav class="abs nav">
    <div class="abs nav-home">
      <svg width="16" height="15" viewBox="0 0 16 15"><path d="M8 1 1 7.5h2V14h3.5V10h3v4H13V7.5h2z" fill="#fff"/></svg>
    </div>
    <div class="abs nav-links">
      <span style="left:0">About</span>
      <span style="left:62px">Portfolio</span>
      <span style="left:135px">Blog</span>
      <span style="left:192px">Shortcodes</span>
      <span style="left:280px">Features</span>
      <span style="left:356px">Pages</span>
      <span style="left:421px">Contact</span>
    </div>
    <div class="abs nav-search">
      <svg width="14" height="14" viewBox="0 0 14 14"><circle cx="5.5" cy="5.5" r="4" fill="none" stroke="#fff" stroke-width="2"/><path d="M8.5 8.5 13 13" stroke="#fff" stroke-width="2.4" stroke-linecap="round"/></svg>
    </div>
  </nav>
</header>

<section class="abs title-band">
  <div class="abs title-tab"><h1>SERVICES</h1></div>
  <div class="abs title-notch"></div>
  <div class="abs tagline">We build highly usable stuff!</div>
  <div class="abs crumbs">Home / About</div>
</section>

<section class="abs offer">
  <h2>WHAT WE OFFER?</h2>
  <p>Lorem ipsum dolor sit amet, consectetur adipisicing elit, sed do eiusmod tempor incididunt ut labore et dolore magna aliqua. Ut enim ad minim veniam, quis nostrud exercitation ullamco laboris nisi ut aliquip ex ea commodo consequat. Duis aute irure dolor in reprehenderit in voluptate velit esse cillum dolore eu fugiat nulla pariatur. Excepteur sint occaecat cupidatat non proident, sunt in culpa qui officia deserunt mollit anim id est laborum.</p>
  <p>Sed ut perspiciatis unde omnis iste natus error sit voluptatem accusantium doloremque laudantium, totam rem aperiam, eaque ipsa quae ab illo inventore veritatis et quasi architecto beatae vitae dicta sunt explicabo.</p>
</section>

<aside class="abs buy">
  <h2>BUY NOW</h2>
  <p>Lorem ipsum dolor sit amet, consectetur adipisicing elit, sed do eiusmod tempor incididunt ut labore et dolore magna aliqua.</p>
</aside>

<article class="abs service" style="left:161px;top:424px">
  <h3>TRAINING</h3>
  <div class="icon" style="top:38px">
    <svg width="46" height="40" viewBox="0 0 46 40"><path d="M3 2v33h40" fill="none" stroke="#63666f" stroke-width="5"/><path d="M11 24l9 6 10-14 10-6" fill="none" stroke="#63666f" stroke-width="4"/><circle cx="20" cy="30" r="4" fill="#63666f"/><circle cx="30" cy="16" r="4" fill="#63666f"/><circle cx="40" cy="10" r="4" fill="#63666f"/></svg>
  </div>
  <div class="copy" style="top:37px">
    <p>Lorem ipsum dolor sit amet, consectetur adipisicing elit, sed do eiusmod , quis nostrud e nisi ut aliquip ex ea commodo consequat.</p>
    <p>Duis aute irure dolor in reprehenderit in voluptate dolore eu fugiat nulla pariatu cepteur sint occaecat cupidatat non proident.</p>
  </div>
</article>

<article class="abs service" style="left:611px;top:424px">
  <h3>RESUMES &amp; CVS</h3>
  <div class="icon" style="top:38px">
    <svg width="36" height="44" viewBox="0 0 36 44"><path d="M2 2h22l10 10v30H2z" fill="#63666f"/><path d="M24 2v10h10" fill="#9a9ca3"/><path d="M8 20h20M8 27h20M8 34h14" stroke="#eff2f0" stroke-width="3"/></svg>
  </div>
  <div class="copy" style="top:37px">
    <p>Lorem ipsum dolor sit amet, consectetur adipisicing elit, sed do eiusmod , quis nostrud e nisi ut aliquip ex ea commodo consequat.</p>
    <p>Duis aute irure dolor in reprehenderit in voluptate dolore eu fugiat nulla pariatu cepteur sint occaecat cupidatat non proident.</p>
  </div>
</article>

<article class="abs service" style="left:161px;top:549px">
  <h3>SKILLS ASSESSMENT</h3>
  <div class="icon" style="top:42px">
    <svg width="40" height="40" viewBox="0 0 40 40"><rect x="2" y="2" width="36" height="36" rx="4" fill="#63666f"/><path d="M10 20l7 7 13-14" fill="none" stroke="#eff2f0" stroke-width="4"/></svg>
  </div>
  <div class="copy" style="top:37px">
    <p>Lorem ipsum dolor sit amet, consectetur adipisicing elit, sed do eiusmod , quis nostrud e nisi ut aliquip ex ea commodo consequat.</p>
    <p>Duis aute irure dolor in reprehenderit in voluptate dolore eu fugiat nulla pariatu cepteur sint occaecat cupidatat non proident.</p>
  </div>
</article>

<article class="abs service" style="left:611px;top:549px">
  <h3>TRAINING EQUIPMENT</h3>
  <div class="icon" style="top:39px">
    <svg width="30" height="44" viewBox="0 0 30 44"><path d="M19 1 2 25h11l-3 18 18-26H17z" fill="#63666f"/></svg>
  </div>
  <div class="copy" style="top:37px">
    <p>Lorem ipsum dolor sit amet, consectetur adipisicing elit, sed do eiusmod , quis nostrud e nisi ut aliquip ex ea commodo consequat.</p>
    <p>Duis aute irure dolor in reprehenderit in voluptate dolore eu fugiat nulla pariatu cepteur sint occaecat cupidatat non proident.</p>
  </div>
</article>

<section class="abs ticker">
  <span class="abs mark"></span>
  <p>Nam libero tempore, cum soluta nobis est eligendi optio cumque nihil impedit quo minus id quod maxime placeat facere possimus, omnis voluptas <b>@torenktraining</b></p>
  <div class="abs arrow prev"><svg width="6" height="9" viewBox="0 0 6 9"><path d="M5 1 1.5 4.5 5 8" fill="none" stroke="#fff" stroke-width="2"/></svg></div>
  <div class="abs arrow next"><svg width="6" height="9" viewBox="0 0 6 9"><path d="M1 1l3.5 3.5L1 8" fill="none" stroke="#fff" stroke-width="2"/></svg></div>
</section>

<footer class="abs footer">
  <h2>GET IN TOUCH</h2>
  <p class="lede">Lorem ipsum dolor sit amet, consectetur adipisicing</p>
  <div class="abs social-foot" aria-label="Social links">
    <span class="dot"></span><span class="dot"></span><span class="dot"></span><span class="dot"></span><span class="dot"></span><span class="dot"></span>
  </div>
  <nav class="abs foot-links" style="left:697px">
    <span style="left:0">Home</span>
    <span style="left:46px">Pages</span>
    <span style="left:93px">Portfolio</span>
    <span style="left:147px">Shortcodes</span>
    <span style="left:215px">Features</span>
    <span style="left:271px">Blog</span>
    <span style="left:310px">Contact</span>
  </nav>
</footer>

<div class="abs legal"><p>Copyright 2014 Toren K Pty Ltd</p></div>

</body>
</html>
```